An Agro-Processor Needs a Packaging Design

We need packaging designs for a range of dried fruits and jams with a family look. The line-up has five variants of dried fruits and five variants of jams (the designs to include front and back of the packaging). The entire range will be marketed under the 'Petalvyn' brand name - please find the logo attached (the logo has a lock-up with the tagline). The packaging format for the dried fruits are resealable stand-up pouches and the jams are glass bottles - please find attached pictures of the packaging formats for reference.

Please find inspiration boards for the packaging design. Also find attached inspiration board for the design style required for the back of the dried fruit packaging.

For the dried fruit packaging, we need to develop a seal that conveys organic and sugar-free claims (please find attached example of a seal)

Target Market(s)

Organic and natural living enthusiasts who would pay a premium to get the best for them and their families

Industry/Entity Type

Food Production

Font styles to use
Sans Serif
Script

Colors

Designer to choose colors to be used in the design.

Requirements
Must have
• - The brand name 'petalvyn' is inspired by the abundance of nature in Africa, it also connotes organic, natural, freshness, delicateness, airiness, sophistication and premium and therefore the design should project these values
• - The design styling to be fun, modern and 'simplistic'
• - Please find below the packaging copy for both dried fruits and jams
• DRIED FRUIT FRONT PACKAGING:
• LOGO: Petalvyn - Sharing Earth's Warmth
• FIVE VARIANT NAMES: Plucky Pineapple | Dreamy Mango | Jolly Banana | Dapper Papaya | Breezy Jackfruit
• Dried
• DEVELOP A SEAL: 100% Organic | No Added Sugar (please see example attached)
• Ugandan Origin
• Net Weight: 100g
• DRIED FRUIT BACK COPY:
• Nature's best tasting fruits are also the healthiest which is why we have made it our mission to spread nature's love! Nourished by the tropical rains on the sun-drenched soils of Africa and cultivated by the caring hands of the local farmers, our organic range of dried fruits are nutrient-dense, high in fiber and rich in minerals. Enjoy them in your salads and cereals or simply relish them as a snack! They are diet-friendly if eaten in moderation and are a natural source of energy.
• VISUAL: Stack of Fruit Visual with arrows, each with the following claims (see examples attached in the inspiration boards):
• - 100% Organic
• - No Added Sugar
• - Nutrient-Dense
• - High in Fiber
• - Rich in Minerals
• INCLUDE: Nutritional Facts Table
• Ingredients: Mango - contains 100% fruit with no added sugars, preservatives, additives, colorings or flavorings.
• Reseal the pack to maintain freshness. Store in a cool and dry place.
• INCLUDE SPACE FOR: Batch Code / Expiry Date
• Barcode
• Produced by: Temari Food Industries, P. O. Box XXXXX, Kampala - Uganda.
• Find out more about us:
• Telephone: +XXX-XXX-XXXXXX
• Email: Info@TemariFoodIndustriez.com
• www.Chatterbook.net/Petalvyn
• JAM FRONT COPY:
• FIVE VARIANT NAMES: Plucky Pineapple with a Hint of Ginger | Dreamy Mango with a Kiss of Vanilla | Jolly Banana with a Twist of Chocolate | Dapper Papaya with a Pinch of Cardamon | Breezy Jackfruit with a Touch of Cinnamon
• Jam
• Ugandan Origin
• Net Weight: 400g
• JAM BACK COPY:
• Nature's best tasting fruits are also the healthiest which is why we have made it our mission to spread nature's love! Our range of jams come from fruits that have been nourished by the tropical rains on the sun-drenched soils of Africa and have been cultivated by the caring hands of the local farmers. We pride ourselves on making sure that the jams taste as delicious and look as natural as the perfectly ripened fruit! We then make it even better by pairing it with a hint of spice! Enjoy them in your breakfast or use them as a filling in baking.
• Ingredients: Mango, citric acid, sugar, pectin, vanilla
• Barcode
• Find out more about us:

```html
<!DOCTYPE html>
<html lang="en">
<head>
<meta charset="utf-8">
<title>Petalvyn Dried Fruit Packaging</title>
<link rel="stylesheet" href="https://fonts.googleapis.com/css2?family=Roboto+Slab:wght@500;700&family=Open+Sans:wght@400;600;700&family=Kalam:wght@400;700&display=swap">
<style>
:root{
  --bg:#efeee6;
  --paper:#ffffff;
  --brown:#5b3b2e;
  --pink:#e0566b;
  --blue:#4aa8c8;
  --blue-light:#9ed6e8;
  --orange:#e0622a;
  --yellow:#f5c11c;
  --jack:#d4a04a;
  --lime:#9cc32a;
  --papaya:#e2697a;
  --seal-green:#1d9a4b;
  --seal-brown:#6a4a3c;
  --text:#3a2a22;
}
*{box-sizing:border-box;margin:0;padding:0}
html,body{width:1200px;height:1000px;overflow:hidden}
body{background:var(--bg);font-family:"Open Sans",sans-serif;color:var(--text);position:relative}
.panel{position:absolute;background:var(--paper);overflow:hidden;box-shadow:0 2px 6px rgba(0,0,0,.12)}
.band{position:absolute;left:0;top:0;width:100%}
.brand{position:absolute;left:0;width:100%;text-align:center}
.brand-name{font-family:"Open Sans",sans-serif;font-weight:600;color:var(--brown);letter-spacing:.5px;display:inline-flex;align-items:center;gap:.25em}
.brand-dot{display:inline-block;border-radius:50%;background:var(--lime)}
.tagline{font-family:"Kalam",cursive;color:var(--pink);display:block}
.pill{position:absolute;background:var(--brown);color:#fff;font-family:"Roboto Slab",serif;font-weight:700;text-align:center;line-height:1;border-radius:50%/50%;display:flex;align-items:center;justify-content:center;z-index:2}
.ring{position:absolute}
.variant{position:absolute;left:0;width:100%;text-align:center;font-family:"Roboto Slab",serif;font-weight:700;line-height:1;z-index:1}
.net{position:absolute;font-weight:700;color:var(--text);line-height:1.2}
.seal{position:absolute;border-radius:50%;background:radial-gradient(circle,var(--seal-green) 0 45%,#fff 46% 80%,var(--seal-brown) 81%);z-index:2}

/* front pouch */
.pouch{left:45px;top:25px;width:580px;height:950px;border-radius:6px}
.pouch .brand{top:190px}
.pouch .brand-name{font-size:92px}
.pouch .brand-dot{width:22px;height:22px}
.pouch .tagline{font-size:31px;margin-top:-14px}
.pouch .pill{left:70px;top:358px;width:190px;height:92px;font-size:28px}
.pouch .ring{left:60px;top:385px;width:480px;height:470px}
.pouch .fruit-wreath{position:absolute;left:135px;top:440px;width:330px;height:330px;border-radius:50%;border:62px solid #f6cf62;opacity:.8}
.pouch .variant{top:560px}
.pouch .variant .line1{font-size:56px}
.pouch .variant .line2{font-size:56px;color:var(--orange);display:block;margin-top:4px}
.pouch .net{left:85px;top:832px;font-size:20px}
.pouch .net b{font-size:24px}
.pouch .seal{left:380px;top:720px;width:140px;height:140px}

/* mini fronts */
.mini{width:180px;height:303px}
.mini .brand{top:58px}
.mini .brand-name{font-size:27px}
.mini .brand-dot{width:7px;height:7px}
.mini .tagline{font-size:10.5px;margin-top:-5px}
.mini .pill{left:24px;top:117px;width:64px;height:30px;font-size:9.5px}
.mini .ring{left:12px;top:120px;width:160px;height:160px}
.mini .variant{top:181px}
.mini .variant .line1{font-size:16px}
.mini .variant .line2{font-size:21px;display:block;margin-top:1px}
.mini .net{left:22px;top:262px;font-size:7px}
.mini .net b{font-size:10px}
.mini .seal{left:125px;top:242px;width:48px;height:48px}
.banana{left:782px;top:27px;--tone:var(--yellow)}
.jackfruit{left:985px;top:27px;--tone:var(--jack)}
.mango{left:985px;top:348px;--tone:var(--lime)}
.papaya{left:985px;top:668px;--tone:var(--papaya)}

/* back label */
.back{left:658px;top:418px;width:297px;height:522px}
.back .brand{top:58px}
.back .brand-name{font-size:34px}
.back .brand-dot{width:8px;height:8px}
.back .tagline{font-size:13px;margin-top:-6px}
.back .pill{left:185px;top:48px;width:68px;height:30px;font-size:9.5px}
.back-story{position:absolute;left:10px;top:132px;width:138px;font-size:8.2px;line-height:1.27;text-align:center}
.claims{position:absolute;left:148px;top:132px;width:145px;height:180px}
.fruit-stack{position:absolute;left:50px;top:50px;width:44px;height:120px;border-radius:6px;background:linear-gradient(180deg,#f5c84a,#e8671e 55%,#f5c84a)}
.claim{position:absolute;font-size:7.6px;font-weight:700;color:#fff;text-align:center;line-height:1.1;border-radius:8px;padding:4px 5px;z-index:1}
.nutrition{position:absolute;left:22px;top:316px;width:122px;border:1px solid var(--lime);border-radius:4px;padding:4px 5px;font-size:5.6px;line-height:1.35}
.nutrition h3{font-size:9px;font-weight:700;line-height:1.1}
.nutrition .row{display:flex;justify-content:space-between}
.nutrition .rule{border-top:1px solid #333;margin:2px 0}
.nutrition .note{font-size:4.6px;margin-top:3px}
.ingredients{position:absolute;left:150px;top:318px;width:138px;font-size:6.4px;line-height:1.3}
.codes{position:absolute;left:150px;top:380px;width:134px;height:37px;border:1px solid var(--lime);border-radius:4px;display:flex}
.codes .code-slot{flex:1}
.codes .batch{flex:1;border-left:1px solid var(--lime);font-size:6px;font-weight:700;padding:4px}
.contact{position:absolute;left:150px;top:424px;width:140px;font-size:6.2px;line-height:1.35}
</style>
</head>
<body>

<section class="panel pouch" aria-label="Dried fruit pouch front, Plucky Pineapple">
  <svg class="band" width="580" height="190" viewBox="0 0 580 190" aria-hidden="true">
    <path d="M0,0H580V120C470,170 330,110 200,140C120,158 50,150 0,135Z" fill="var(--blue-light)"/>
    <path d="M0,0H580V95C470,140 330,85 200,112C120,128 50,120 0,108Z" fill="var(--blue)"/>
  </svg>
  <div class="brand">
    <span class="brand-name">petalvyn<span class="brand-dot"></span></span>
    <span class="tagline">Sharing Earth's Warmth</span>
  </div>
  <svg class="ring" viewBox="0 0 480 470" aria-hidden="true">
    <ellipse cx="240" cy="240" rx="215" ry="208" fill="none" stroke="var(--blue)" stroke-width="14" opacity=".8"/>
    <ellipse cx="248" cy="232" rx="222" ry="214" fill="none" stroke="var(--blue-light)" stroke-width="8"/>
  </svg>
  <div class="fruit-wreath" role="img" aria-label="Wreath of dried pineapple slices"></div>
  <div class="pill">DRIED<br>FRUIT</div>
  <div class="variant">
    <span class="line1"><span style="color:#27a9d8">P</span><span style="color:#3db54a">l</span><span style="color:#f5b21c">u</span><span style="color:#e0622a">c</span><span style="color:#27a9d8">k</span><span style="color:#3db54a">y</span></span>
    <span class="line2">Pineapple</span>
  </div>
  <div class="net">Net Weight:<br><b>100g</b></div>
  <div class="seal" role="img" aria-label="Seal: 100% Organic, Ugandan Origin, No Added Sugar"></div>
</section>

<section class="panel back" aria-label="Dried fruit pouch back">
  <svg class="band" width="297" height="50" viewBox="0 0 297 50" aria-hidden="true">
    <path d="M0,0H297V32C230,48 160,26 90,36C50,42 20,40 0,34Z" fill="var(--blue-light)"/>
    <path d="M0,0H297V22C230,36 160,16 90,26C50,32 20,30 0,24Z" fill="var(--blue)"/>
  </svg>
  <div class="pill">DRIED<br>FRUIT</div>
  <div class="brand">
    <span class="brand-name">petalvyn<span class="brand-dot"></span></span>
    <span class="tagline">Sharing Earth's Warmth</span>
  </div>
  <p class="back-story">Nature's best tasting fruits are also the healthiest which is why we have made it our mission to spread nature's love! Nourished by the tropical rains on the sun-drenched soils of Africa and cultivated by the caring hands of the local farmers, our organic range of dried fruits are nutrient-dense, high in fiber and rich in minerals. Enjoy them in your salads and cereals or simply relish them as a snack! They are diet-friendly if eaten in moderation and are a natural source of energy.</p>
  <div class="claims">
    <svg width="145" height="180" viewBox="0 0 145 180" style="position:absolute;left:0;top:0" aria-hidden="true">
      <g fill="none" stroke="#2e8b3e" stroke-width="1" stroke-dasharray="2 2">
        <path d="M38,36 C45,50 50,58 54,66"/>
        <path d="M102,36 C98,48 94,56 90,66"/>
        <path d="M112,80 C104,88 98,92 92,96"/>
        <path d="M40,125 C46,120 50,116 54,112"/>
        <path d="M110,150 C104,142 98,136 92,130"/>
      </g>
    </svg>
    <div class="fruit-stack" role="img" aria-label="Stack of dried fruit pieces"></div>
    <div class="claim" style="left:16px;top:8px;background:#3db54a">100%<br>Organic</div>
    <div class="claim" style="left:86px;top:8px;background:#5b78c2">No Added<br>Sugar</div>
    <div class="claim" style="left:104px;top:68px;background:var(--orange)">Nutrient<br>Dense</div>
    <div class="claim" style="left:8px;top:112px;background:#3db54a">High in<br>Fiber</div>
    <div class="claim" style="left:98px;top:138px;background:#a06bc4">Rich in<br>Minerals</div>
  </div>
  <div class="nutrition">
    <h3>Nutrition Facts</h3>
    <div>Serving Size 16 pieces (42g)</div>
    <div class="rule"></div>
    <div>Amount Per Serving</div>
    <div class="row"><span>Calories 150</span><span>Calories from Fat 0</span></div>
    <div class="row"><span></span><span>% Daily Values*</span></div>
    <div class="rule"></div>
    <div class="row"><b>Total Fat 0 g</b><span>0 %</span></div>
    <div class="row"><span>&nbsp;Saturated Fat -</span><span></span></div>
    <div class="row"><span>Cholesterol 0 mg</span><span>0 %</span></div>
    <div class="row"><span>Sodium 10 mg</span><span>0 %</span></div>
    <div class="row"><b>Total Carbohydrate 36g</b><span>12 %</span></div>
    <div class="row"><span>&nbsp;Dietary Fiber 2 g</span><span>8 %</span></div>
    <div class="row"><span>&nbsp;Sugar 24 g</span><span></span></div>
    <div class="row"><span>Protein 0 g</span><span></span></div>
    <div class="rule"></div>
    <div class="row"><span>Vitamin A -</span><span>Vitamin C 15 %</span></div>
    <div class="row"><span>Calcium -</span><span>Iron -</span></div>
    <div class="note">* Percent Daily Values are based on a 2000 calorie diet. Your daily values may be higher or lower depending on your calorie needs.</div>
  </div>
  <div class="ingredients"><b>Ingredients:</b><br><b>Mango. Contains 100% fruit with no added sugars, preservatives, additives, colorings or flavorings.<br>Reseal the pack to maintain freshness.<br>Store in a cool and dry place.</b></div>
  <div class="codes"><div class="code-slot"></div><div class="batch">Batch Code /<br>Expiry Date:</div></div>
  <div class="contact">Produced by: <b>Temari Food Industries</b><br>P. O. Box XXXXX, Kampala - Uganda.<br>Find out more about us:<br>Telephone: +XXX-XXX-XXXXXX<br>Email: Info@TemariFoodIndustriez.com<br>www.Chatterbook.net/Petalvyn</div>
</section>

<section class="panel mini banana" aria-label="Front label, Jolly Banana">
  <svg class="band" width="180" height="44" viewBox="0 0 180 44" aria-hidden="true">
    <path d="M0,0H180V34C140,44 95,26 55,34C30,38 12,36 0,32Z" fill="#fbe08a"/>
    <path d="M0,0H180V24C140,34 95,16 55,24C30,28 12,26 0,22Z" fill="var(--tone)"/>
  </svg>
  <div class="brand"><span class="brand-name">petalvyn<span class="brand-dot"></span></span><span class="tagline">Sharing Earth's Warmth</span></div>
  <svg class="ring" viewBox="0 0 160 160" role="img" aria-label="Wreath of dried banana slices">
    <circle cx="82" cy="82" r="68" fill="none" stroke="var(--tone)" stroke-width="7"/>
    <circle cx="82" cy="82" r="50" fill="none" stroke="#f7d98a" stroke-width="26" opacity=".8"/>
  </svg>
  <div class="pill">DRIED<br>FRUIT</div>
  <div class="variant"><span class="line1" style="color:#3db54a">Jolly</span><span class="line2" style="color:#b5652a">Banana</span></div>
  <div class="net">Net Weight:<br><b>100g</b></div>
  <div class="seal" role="img" aria-label="Seal: 100% Organic, Ugandan Origin, No Added Sugar"></div>
</section>

<section class="panel mini jackfruit" aria-label="Front label, Breezy Jackfruit">
  <svg class="band" width="180" height="44" viewBox="0 0 180 44" aria-hidden="true">
    <path d="M0,0H180V34C140,44 95,26 55,34C30,38 12,36 0,32Z" fill="#ecd3a4"/>
    <path d="M0,0H180V24C140,34 95,16 55,24C30,28 12,26 0,22Z" fill="var(--tone)"/>
  </svg>
  <div class="brand"><span class="brand-name">petalvyn<span class="brand-dot"></span></span><span class="tagline">Sharing Earth's Warmth</span></div>
  <svg class="ring" viewBox="0 0 160 160" role="img" aria-label="Wreath of dried jackfruit pieces">
    <circle cx="82" cy="82" r="68" fill="none" stroke="var(--tone)" stroke-width="7"/>
    <circle cx="82" cy="82" r="50" fill="none" stroke="#f5c234" stroke-width="26" opacity=".8"/>
  </svg>
  <div class="pill">DRIED<br>FRUIT</div>
  <div class="variant"><span class="line1" style="color:#e8891e">Breezy</span><span class="line2" style="color:#a8622a">Jackfruit</span></div>
  <div class="net">Net Weight:<br><b>100g</b></div>
  <div class="seal" role="img" aria-label="Seal: 100% Organic, Ugandan Origin, No Added Sugar"></div>
</section>

<section class="panel mini mango" aria-label="Front label, Dreamy Mango">
  <svg class="band" width="180" height="44" viewBox="0 0 180 44" aria-hidden="true">
    <path d="M0,0H180V34C140,44 95,26 55,34C30,38 12,36 0,32Z" fill="#d4e68e"/>
    <path d="M0,0H180V24C140,34 95,16 55,24C30,28 12,26 0,22Z" fill="var(--tone)"/>
  </svg>
  <div class="brand"><span class="brand-name">petalvyn<span class="brand-dot"></span></span><span class="tagline">Sharing Earth's Warmth</span></div>
  <svg class="ring" viewBox="0 0 160 160" role="img" aria-label="Wreath of dried mango slices">
    <circle cx="82" cy="82" r="68" fill="none" stroke="var(--tone)" stroke-width="7"/>
    <circle cx="82" cy="82" r="50" fill="none" stroke="#f6a93a" stroke-width="26" opacity=".8"/>
  </svg>
  <div class="pill">DRIED<br>FRUIT</div>
  <div class="variant"><span class="line1" style="color:#e0622a">Dreamy</span><span class="line2" style="color:#1f8a4a">Mango</span></div>
  <div class="net">Net Weight:<br><b>100g</b></div>
  <div class="seal" role="img" aria-label="Seal: 100% Organic, Ugandan Origin, No Added Sugar"></div>
</section>

<section class="panel mini papaya" aria-label="Front label, Dapper Papaya">
  <svg class="band" width="180" height="44" viewBox="0 0 180 44" aria-hidden="true">
    <path d="M0,0H180V34C140,44 95,26 55,34C30,38 12,36 0,32Z" fill="#f2b4bc"/>
    <path d="M0,0H180V24C140,34 95,16 55,24C30,28 12,26 0,22Z" fill="var(--tone)"/>
  </svg>
  <div class="brand"><span class="brand-name">petalvyn<span class="brand-dot"></span></span><span class="tagline">Sharing Earth's Warmth</span></div>
  <svg class="ring" viewBox="0 0 160 160" role="img" aria-label="Wreath of dried papaya strips">
    <circle cx="82" cy="82" r="68" fill="none" stroke="var(--tone)" stroke-width="7"/>
    <circle cx="82" cy="82" r="50" fill="none" stroke="#f08a2a" stroke-width="26" opacity=".8"/>
  </svg>
  <div class="pill">DRIED<br>FRUIT</div>
  <div class="variant"><span class="line1" style="color:#d6297a">Dapper</span><span class="line2" style="color:#e0622a">Papaya</span></div>
  <div class="net">Net Weight:<br><b>100g</b></div>
  <div class="seal" role="img" aria-label="Seal: 100% Organic, Ugandan Origin, No Added Sugar"></div>
</section>

</body>
</html>
```